Website for Velmorund Capital, my new firm that raises money from investors to buy, build, own an...

Velmorund Capital needs a website! We are a new company with very experienced people, who invest in, own and build hotel properties, as well as apartments and other commercial real estate. We seek investors for our projects, and we provide safe, secure returns on their investment in our projects. Our new logo is designed to exhibit strength, class and security, and would like our website to continue on this theme. Our name, Velmorund, is a word-play on a Greek word “aristeia”, which means “excellence” and “a warriors finest moment of glory in war”. If you are in business, you realize that much of it is like war, with strategy and moves and opponents and competitors, and ever-changing economic conditions and threats that make business very much like war. We like to think that we are good at business (war), and so have named our company “Velmorund”, using the founders last name and the word “aristeia” combined. Another definition of "aristeia" is "performing at the peak of one's potential after a long struggle"...again, much like business in real life! The website design should exhibit financial security, smart moves, and positive growth towards a bright future.

Target Market(s)

The target market is smart and wealthy investors, with others such as brokers, cities and government agencies, lenders, sellers, partners, etc also looking at it.

Industry/Entity Type

Investment

Number of Pages Required

5+ page

Font styles to use
Sans Serif

Colors
fec214

Requirements
Must have
• Our website should have a landing page, a "about" or bio page, a projects page and a contact us page. Our new logo uses the colors black and gold, so this should be factored in to our site. The site should be simple, yet impactful and impressive. I have actually two logos, which can be mixed and interchanged in a complimentary way, each with their own unique look.
Nice to have
• I have uploaded a couple screenshots of a website i like, and the simplicity I mention.
Should not have
• The site should not be flashy or complicated or complex or "busy"

```html
<!DOCTYPE html>
<html lang="en">
<head>
<meta charset="utf-8">
<title>Velmorund Capital</title>
<link rel="stylesheet" href="https://fonts.googleapis.com/css2?family=Montserrat:wght@400;500;600;700&family=Exo+2:wght@600;700&family=Didact+Gothic&display=swap">
<style>
:root{
  --gold:#c4952f;
  --gold-soft:#d2a84b;
  --ink:#111111;
  --text:#555555;
  --white:#ffffff;
  --footer:#0d0d0d;
  --footer-bottom:#000000;
  --footer-text:#c9c9c9;
}
*{margin:0;padding:0;box-sizing:border-box}
html,body{width:753px;height:1200px;overflow:hidden;background:var(--white)}
body{position:relative;font-family:"Didact Gothic",sans-serif;color:var(--text)}
.abs{position:absolute}
/* header */
.site-header{position:absolute;left:0;top:0;width:753px;height:85px}
.social{position:absolute;display:flex;gap:4px}
.social span{width:26px;height:26px;border-radius:50%;border:1.5px solid var(--gold)}
.social span.filled{background:var(--gold)}
.brand{position:absolute;left:0;width:753px;top:32px;text-align:center;font-family:"Montserrat",sans-serif;font-weight:600;font-size:16px;letter-spacing:1px;color:var(--ink)}
.call{position:absolute;left:578px;top:27px;display:flex;gap:8px;align-items:flex-start}
.call-label{font-family:"Montserrat",sans-serif;font-size:9.5px;color:#333}
.call-number{font-family:"Exo 2",sans-serif;font-size:12px;color:var(--gold);letter-spacing:1px;margin-top:2px}
/* nav */
.main-nav{position:absolute;left:0;top:85px;width:753px;height:39px;background:var(--gold);display:flex;justify-content:center;align-items:center;gap:22px;font-family:"Montserrat",sans-serif;font-size:10px;color:var(--white)}
.main-nav .active::before{content:"";display:inline-block;width:4px;height:4px;border-radius:50%;background:var(--white);margin-right:7px;vertical-align:middle}
/* hero */
.hero{position:absolute;left:0;top:124px;width:753px;height:301px;background:linear-gradient(180deg,#4b5868 0%,#7b8591 45%,#b9b2a6 70%,#5b514b 100%)}
.hero-caption{position:absolute;left:0;bottom:0;width:753px;height:45px;background:rgba(20,20,20,.45);display:flex;justify-content:center;align-items:center;gap:22px}
.hero-caption h2{font-family:"Exo 2",sans-serif;font-weight:700;font-size:16px;color:var(--white);letter-spacing:.3px}
/* welcome */
.welcome{position:absolute;left:0;top:463px;width:753px;text-align:center}
.eyebrow{font-family:"Montserrat",sans-serif;font-weight:500;font-size:12.5px;color:var(--gold)}
.welcome h1{font-family:"Montserrat",sans-serif;font-weight:600;font-size:25px;color:var(--ink);letter-spacing:.5px;margin-top:4px}
.welcome p{width:510px;margin:9px auto 0;font-size:8.5px;line-height:17px}
.service{position:absolute;top:591px;width:160px;text-align:center}
.service-icon{width:59px;height:59px;border-radius:50%;background:var(--gold);margin:0 auto;display:flex;align-items:center;justify-content:center}
.service h3{font-family:"Montserrat",sans-serif;font-weight:500;font-size:9.5px;color:var(--ink);margin-top:11px}
.service p{font-size:8.5px;line-height:14.5px;margin-top:3px;padding:0 20px}
/* projects */
.projects{position:absolute;left:0;top:745px;width:753px;height:242px;background:linear-gradient(180deg,#cfa23f 0%,#c2983c 50%,#b88f36 100%)}
.projects h2{position:absolute;left:0;width:753px;top:37px;text-align:center;font-family:"Exo 2",sans-serif;font-weight:600;font-size:26px;color:var(--white)}
.project{position:absolute;top:87px;width:157px;height:118px}
.arrow{position:absolute;top:137px}
/* footer */
.site-footer{position:absolute;left:0;top:987px;width:753px;height:175px;background:var(--footer);color:var(--footer-text);font-size:8.5px}
.footer-brand{position:absolute;left:64px;width:120px;top:48px;text-align:center;font-family:"Montserrat",sans-serif;font-weight:600;font-size:13px;letter-spacing:1px;color:var(--white)}
.footer-col h4{position:absolute;top:27px;font-family:"Montserrat",sans-serif;font-weight:500;font-size:10.5px;color:var(--gold)}
.sitemap{position:absolute;left:216px;top:52px;list-style:none}
.sitemap li{height:18.5px;font-size:8.5px}
.sitemap li::before{content:"";display:inline-block;width:4px;height:4px;border-radius:50%;background:var(--gold);margin-right:10px;vertical-align:middle}
.contact-row{position:absolute;left:380px;display:flex;align-items:center;gap:10px;width:170px;line-height:13px}
.contact-icon{flex:none;width:27px;height:27px;border-radius:50%;border:1.5px solid var(--gold);display:flex;align-items:center;justify-content:center}
.newsletter-text{position:absolute;left:549px;top:57px;width:160px;line-height:13px}
.email-field{position:absolute;left:547px;top:87px;width:157px;height:27px;background:var(--white);color:#555;font-size:8.5px;padding:9px 10px}
.subscribe{position:absolute;left:548px;top:116px;width:97px;height:26px;background:var(--gold);color:var(--white);font-family:"Exo 2",sans-serif;font-weight:700;font-size:12.5px;display:flex;align-items:center;justify-content:center;letter-spacing:.4px}
.copyright{position:absolute;left:0;top:1162px;width:753px;height:38px;background:var(--footer-bottom);color:#aaa;font-size:8.5px;text-align:center;line-height:38px}
.copyright b{color:var(--white);font-weight:400}
</style>
</head>
<body>

<header class="site-header">
  <div class="social" style="left:49px;top:29px"><span class="filled"></span><span></span><span></span></div>
  <div class="brand">VELMORUND</div>
  <div class="call">
    <svg width="26" height="26" viewBox="0 0 24 24"><path fill="#c4952f" d="M6.6 10.8a15 15 0 0 0 6.6 6.6l2.2-2.2c.3-.3.7-.4 1-.2 1.1.4 2.3.6 3.6.6.6 0 1 .4 1 1V20c0 .6-.4 1-1 1A17 17 0 0 1 3 4c0-.6.4-1 1-1h3.5c.6 0 1 .4 1 1 0 1.3.2 2.5.6 3.6.1.3 0 .7-.2 1z"/></svg>
    <div><div class="call-label">Call Us Today :</div><div class="call-number">555 014 2368</div></div>
  </div>
</header>

<nav class="main-nav">
  <span class="active">HOME</span><span>ABOUT US</span><span>PROJECTS</span><span>CONTACT US</span>
</nav>

<section class="hero" role="img" aria-label="Photo of a modern multi-storey hotel building under a cloudy sky">
  <div class="hero-caption">
    <svg width="10" height="18" viewBox="0 0 10 18"><path d="M9 1 1 9l8 8" fill="none" stroke="#ddd" stroke-width="1.2"/></svg>
    <h2>WE PROVIDE SAFE, SECURE RETURNS</h2>
    <svg width="10" height="18" viewBox="0 0 10 18"><path d="m1 1 8 8-8 8" fill="none" stroke="#ddd" stroke-width="1.2"/></svg>
  </div>
</section>

<section class="welcome">
  <div class="eyebrow">WELCOME TO</div>
  <h1>VELMORUND CAPITAL</h1>
  <p>Lorem Ipsum is simply dummy text of the printing and typesetting industry. Lorem Ipsum has been the industry's standard dummy text ever since the 1500s, when an unknown printer took a galley of type and scrambled it to make a type specimen book It has survived not only five centuries</p>
</section>

<div class="service" style="left:146px">
  <div class="service-icon"><svg width="30" height="34" viewBox="0 0 30 34" fill="#fff"><rect x="4" y="4" width="10" height="28"/><rect x="14" y="12" width="12" height="20"/><g fill="#c4952f"><rect x="6" y="8" width="2" height="3"/><rect x="10" y="8" width="2" height="3"/><rect x="6" y="14" width="2" height="3"/><rect x="10" y="14" width="2" height="3"/><rect x="17" y="16" width="2" height="3"/><rect x="21" y="16" width="2" height="3"/><rect x="17" y="22" width="2" height="3"/><rect x="21" y="22" width="2" height="3"/></g></svg></div>
  <h3>BUILD HOTEL PROPERTIES</h3>
  <p>Lorem Ipsum is simply dummy text of the printing.</p>
</div>
<div class="service" style="left:296px">
  <div class="service-icon"><svg width="28" height="34" viewBox="0 0 28 34" fill="#fff"><rect x="4" y="3" width="20" height="29"/><g fill="#c4952f"><rect x="7" y="7" width="14" height="2"/><rect x="7" y="12" width="14" height="2"/><rect x="7" y="17" width="14" height="2"/><rect x="11" y="24" width="6" height="8"/></g></svg></div>
  <h3>APARTMENTS</h3>
  <p>Lorem Ipsum is simply dummy text of the printing.</p>
</div>
<div class="service" style="left:448px">
  <div class="service-icon"><svg width="34" height="32" viewBox="0 0 34 32" fill="#fff"><path d="M17 2 2 14h4v16h22V14h4z"/><g fill="#c4952f"><rect x="10" y="16" width="4" height="4"/><rect x="20" y="16" width="4" height="4"/><rect x="15" y="22" width="4" height="8"/></g></svg></div>
  <h3>COMMERCIAL REAL ESTATE</h3>
  <p>Lorem Ipsum is simply dummy text of the printing.</p>
</div>

<section class="projects" role="img" aria-label="Gold-toned city skyline backdrop">
  <h2>OUR PROJECTS</h2>
  <svg class="arrow" style="left:30px" width="10" height="20" viewBox="0 0 10 20"><path d="M9 1 1 10l8 9" fill="none" stroke="#fff" stroke-width="1.5"/></svg>
  <div class="project" style="left:49px;background:linear-gradient(180deg,#2b3240,#5a3c30 60%,#2a2a28)" role="img" aria-label="Brick apartment building at dusk">
    <svg width="157" height="118" viewBox="0 0 157 118"><circle cx="78" cy="61" r="17" fill="rgba(0,0,0,.3)" stroke="#fff" stroke-width="1.5"/><circle cx="76" cy="59" r="5" fill="none" stroke="#fff" stroke-width="2"/><path d="m80 63 5 5" stroke="#fff" stroke-width="2.5"/></svg>
  </div>
  <div class="project" style="left:215px;background:linear-gradient(180deg,#7fb4e6,#5d8fb5 55%,#8a9a7a)" role="img" aria-label="Glass office building under blue sky"></div>
  <div class="project" style="left:381px;background:linear-gradient(180deg,#6e93b8,#3d3a38 50%,#1f1c1a)" role="img" aria-label="Modern apartment block with balconies"></div>
  <div class="project" style="left:548px;background:linear-gradient(180deg,#8a97a8,#5c6a7a 55%,#3b3a36)" role="img" aria-label="Large glass commercial complex at twilight"></div>
  <svg class="arrow" style="left:714px" width="10" height="20" viewBox="0 0 10 20"><path d="m1 1 8 9-8 9" fill="none" stroke="#fff" stroke-width="1.5"/></svg>
</section>

<footer class="site-footer">
  <div class="footer-brand">VELMORUND</div>
  <div class="social" style="left:80px;top:97px"><span class="filled"></span><span></span><span></span></div>

  <div class="footer-col"><h4 style="left:216px">SITEMAP</h4></div>
  <ul class="sitemap"><li>Home</li><li>About Us</li><li>Projects</li><li>Contact Us</li></ul>

  <div class="footer-col"><h4 style="left:382px">CONTCT US</h4></div>
  <div class="contact-row" style="top:52px">
    <div class="contact-icon"><svg width="12" height="14" viewBox="0 0 12 14"><path d="M6 0a5 5 0 0 0-5 5c0 4 5 9 5 9s5-5 5-9a5 5 0 0 0-5-5z" fill="#c4952f"/><circle cx="6" cy="5" r="1.8" fill="#0d0d0d"/></svg></div>
    <span>101 - lorem ipsum simple text simple dummy text.</span>
  </div>
  <div class="contact-row" style="top:90px">
    <div class="contact-icon"><svg width="13" height="13" viewBox="0 0 24 24"><path fill="#c4952f" d="M6.6 10.8a15 15 0 0 0 6.6 6.6l2.2-2.2c.3-.3.7-.4 1-.2 1.1.4 2.3.6 3.6.6.6 0 1 .4 1 1V20c0 .6-.4 1-1 1A17 17 0 0 1 3 4c0-.6.4-1 1-1h3.5c.6 0 1 .4 1 1 0 1.3.2 2.5.6 3.6.1.3 0 .7-.2 1z"/></svg></div>
    <span>+1 555 014 2368</span>
  </div>
  <div class="contact-row" style="top:124px">
    <div class="contact-icon"><svg width="13" height="10" viewBox="0 0 13 10"><rect width="13" height="10" rx="1" fill="#c4952f"/><path d="m1 1 5.5 4.5L12 1" fill="none" stroke="#0d0d0d" stroke-width="1.2"/></svg></div>
    <span>info@velmorund.com</span>
  </div>

  <div class="footer-col"><h4 style="left:549px">NEWSLETTER</h4></div>
  <p class="newsletter-text">Would you like to recieve our exclusive news and updates !</p>
  <div class="email-field">Enter Email *</div>
  <div class="subscribe">SUBSCRIBE</div>
</footer>

<div class="copyright">© <b>VELMORUND CAPITAL</b> - 2018 All Right Reserved.</div>

</body>
</html>
```